Upsell Vertical Banner Ad Design For B2B Marketing Agency Vertical 768px × 1180px IS THE SIZE

I need a banner made for my website www.brightlanepromotionhub.biz This banner will be an upsell advertisement for after someone signs up for my monthly program. When they login to their account for the 1st time I will give them the chance to upgrade their account to our annual program with just one click.

this is a page that upsells it currently to give you an idea how we market ourselves:
https://tlpx.pagevault-example.com/page/tlp-annual-upsell

Use this content:

Are You Ready To Commit To Taking Your Business To The Next Level?

Because We're In This For The Long-Haul and Dedicated To Your Success...

Save $300 By Upgrading To An Annual Membership And Pay Only $74/mth

((BUTTON))Yes, Upgrade My Plan Right Now!

*Must prepay the full year at only $898/yr!

Target Market(s)

business owners

Industry/Entity Type

Marketing

Requirements
Must have
• 768px × 1180px IS THE SIZE vertical

Use this content:

Nice to have
• Use this content:

Should not have
• Use this content:

```html
<!DOCTYPE html>
<html lang="en">
<head>
<meta charset="utf-8">
<title>Brightlane Promotion Hub – Annual Upgrade</title>
<link rel="stylesheet" href="https://fonts.googleapis.com/css2?family=Poppins:wght@400;500;600;700&display=swap">
<style>
  :root {
    --bg: #ececec;
    --header-bg: #efefef;
    --rule: #d6d6d6;
    --ink: #0d0d0d;
    --brand-blue: #1b74c1;
    --accent-blue: #1b74c1;
    --cta-green: #40cc4c;
    --white: #ffffff;
  }
  html, body {
    margin: 0;
    padding: 0;
    width: 781px;
    height: 1200px;
    overflow: hidden;
    background: var(--bg);
  }
  .banner {
    position: relative;
    width: 768px;
    height: 1180px;
    transform: scale(1.0169);
    transform-origin: 0 0;
    background: radial-gradient(ellipse at 50% 40%, #f1f1f1 0%, var(--bg) 70%);
    font-family: "Poppins", sans-serif;
    color: var(--ink);
    overflow: hidden;
  }
  .site-header {
    position: absolute;
    top: 0; left: 0;
    width: 768px;
    height: 103px;
    background: var(--header-bg);
    border-bottom: 2px solid var(--rule);
    display: flex;
    align-items: center;
    justify-content: center;
  }
  .brand {
    display: flex;
    align-items: center;
    gap: 12px;
  }
  .brand-mark {
    width: 36px;
    height: 36px;
    background: var(--brand-blue);
    border-radius: 4px;
  }
  .brand-name {
    font-weight: 600;
    font-size: 26px;
    letter-spacing: 1px;
    color: var(--brand-blue);
    text-transform: uppercase;
  }
  .copy {
    position: absolute;
    left: 0;
    width: 768px;
    margin: 0;
    text-align: center;
    white-space: nowrap;
  }
  .headline {
    top: 166px;
    font-weight: 700;
    font-size: 40px;
    line-height: 54px;
  }
  .subhead {
    top: 363px;
    font-weight: 400;
    font-size: 29px;
    line-height: 43px;
  }
  .offer-highlight {
    top: 522px;
    font-weight: 600;
    font-size: 51px;
    line-height: 72px;
    color: var(--accent-blue);
  }
  .offer-detail {
    top: 730px;
    font-weight: 600;
    font-size: 35px;
    line-height: 50px;
  }
  .prepay-note {
    top: 866px;
    font-weight: 400;
    font-size: 29px;
    line-height: 36px;
  }
  .cta-button {
    position: absolute;
    top: 996px;
    left: 72px;
    width: 625px;
    height: 92px;
    background: var(--cta-green);
    border-radius: 8px;
    color: var(--white);
    font-family: "Poppins", sans-serif;
    font-weight: 700;
    font-size: 30px;
    text-transform: uppercase;
    letter-spacing: -0.5px;
    display: flex;
    align-items: center;
    justify-content: center;
    text-decoration: none;
    white-space: nowrap;
  }
</style>
</head>
<body>
  <main class="banner">
    <header class="site-header">
      <div class="brand">
        <span class="brand-mark"></span>
        <span class="brand-name">Brightlane Promotion Hub</span>
      </div>
    </header>

    <h1 class="copy headline">Are You Ready To Commit To<br>Taking Your Business To The<br>Next Level?</h1>

    <p class="copy subhead">Because We're In This For The Long-Haul and<br>Dedicated To Your Success...</p>

    <p class="copy offer-highlight">Save $300 And<br>Pay Only $74/mth</p>

    <p class="copy offer-detail">Save $300 By Upgrading To An Annual<br>Membership And Pay Only $74/mth</p>

    <p class="copy prepay-note">Must prepay the full year at only $898/yr!</p>

    <a class="cta-button" href="#upgrade">Yes, Upgrade My Plan Right Now!</a>
  </main>
</body>
</html>
```